Flyer
Zielgruppe
Wir sind Hersteller von Unterkonstruktion für PV-Anlagen. Unsere Zielgruppe sind Monteure oder Firmen die PV-Anlagen verbauen.
Aufgabenstellung
Ich hätte gerne einen Slogan wie Bestpreisgarantie. Oder: Unterkonstruktionen in bester Qualität – zum besten Preis
Oder Sie haben selbst Vorschläge; Wenn möglich können Sie gerne die Bilder von der pptx Datei nehmen. Wir haben auf den Clip unter der Hammerkopfschraube ein Patent (liegt bei), dieser Clip ist ein deutlicher Vorteil bei der Verbauung, damit sich die Hammerkopfschraube beim Verbauen nicht verdreht.
Unsere Adresse sollte noch auf den Flyer:
KT Sonnwerk Energy GmbH, Haselgrundweg 14, 80469 München
Fon: 089 315 884 27 Mail: info@ktsonnwerk-example.com
Website: www.ktsonnwerk-example.com

```html
<!DOCTYPE html>
<html lang="de">
<head>
<meta charset="utf-8">
<title>KT Sonnwerk Energy – Flyer</title>
<link rel="stylesheet" href="https://fonts.googleapis.com/css2?family=Jost:wght@400;500;600&family=Fira+Sans+Condensed:wght@500;700&family=Fira+Sans:wght@500&display=swap">
<style>
  :root {
    --bg: #ebebeb;
    --paper: #ffffff;
    --brand-dark: #1f4e86;
    --brand: #3f62a3;
    --brand-light: #7f9cd0;
    --brand-pale: #c6d3ec;
    --text: #1b1b1b;
    --sky-top: #6f92c4;
    --sky-bottom: #d9e3ee;
    --panel-blue: #2c3f78;
    --roof: #8b8f95;
  }
  * { margin: 0; padding: 0; box-sizing: border-box; }
  html, body { width: 1200px; height: 1200px; overflow: hidden; background: var(--bg); }
  body { position: relative; font-family: "Jost", sans-serif; color: var(--text); }

  .page {
    position: absolute; top: 233px; width: 476px; height: 675px;
    background: var(--paper); overflow: hidden;
  }
  .page--front { left: 100px; }
  .page--back { left: 628px; }

  /* Front */
  .brand { position: absolute; right: 26px; top: 78px; display: flex; align-items: center; gap: 8px; }
  .brand__mark { width: 14px; height: 14px; background: var(--brand-dark); }
  .brand__name { font-family: "Jost", sans-serif; font-weight: 400; font-size: 15px; letter-spacing: 0.6px; color: var(--brand-dark); }
  .tagline {
    position: absolute; right: 27px; top: 125px;
    font-size: 15.5px; font-weight: 500; color: var(--brand);
  }
  .hero-photo {
    position: absolute; left: 0; top: 157px; width: 476px; height: 518px;
    background: linear-gradient(180deg, var(--sky-top) 0%, var(--sky-bottom) 28%, #a7b0a4 40%, var(--panel-blue) 55%, #34488a 75%, var(--roof) 100%);
  }
  .banner { position: absolute; left: 0; top: 0; }
  .offer { position: absolute; left: 160px; top: 292px; color: #fff; }
  .offer__title {
    font-family: "Fira Sans Condensed", sans-serif; font-weight: 700;
    font-size: 30px; letter-spacing: 0.8px; line-height: 1;
  }
  .offer__sub {
    font-family: "Fira Sans", sans-serif; font-weight: 500;
    font-size: 19px; line-height: 24px; margin-top: 4px;
  }

  /* Back */
  .work-photo {
    position: absolute; left: 0; top: 0; width: 237px; height: 278px;
    background: linear-gradient(150deg, #c9ccd3 0%, #3b4d86 40%, #2d2f36 65%, #8a8c70 100%);
  }
  .product-photo {
    position: absolute; left: 237px; top: 397px; width: 239px; height: 278px;
    background: linear-gradient(160deg, var(--brand-pale) 0%, #dfe6f4 60%, #b9c8e6 100%);
  }
  .info { position: absolute; width: 190px; }
  .info__title { font-weight: 600; font-size: 13px; margin-bottom: 14px; }
  .info p { font-size: 9.4px; line-height: 12.6px; margin-bottom: 12px; }
  .info--top { left: 262px; top: 47px; }
  .info--bottom { left: 37px; top: 436px; }

  .contact { position: absolute; left: 37px; top: 292px; color: #fff; }
  .contact__title { font-family: "Fira Sans", sans-serif; font-weight: 500; font-size: 20px; margin-bottom: 6px; }
  .contact__line { font-size: 10px; line-height: 13px; }
  .contact__line--strong { font-weight: 600; }
</style>
</head>
<body>

<section class="page page--front">
  <div class="brand">
    <span class="brand__mark"></span>
    <span class="brand__name">KT SONNWERK ENERGY</span>
  </div>
  <p class="tagline">Nachhaltige Unterkonstruktionen für eine standhafte Zukunft</p>

  <div class="hero-photo" role="img" aria-label="Foto: Dachfläche mit Reihen von Solarmodulen unter bewölktem Himmel"></div>

  <svg class="banner" width="476" height="675" viewBox="0 0 476 675" aria-hidden="true">
    <polygon points="87,356 476,356 476,417 62,417" fill="var(--brand-light)"/>
    <polygon points="160,278 476,278 476,397 98,397" fill="var(--brand)"/>
    <polygon points="424,353 476,353 476,375 414,375" fill="#ffffff"/>
  </svg>

  <div class="offer">
    <h1 class="offer__title">BESTPREISGARANTIE</h1>
    <p class="offer__sub">Unterkonstruktionen in bester<br>Qualität – zum besten Preis</p>
  </div>
</section>

<section class="page page--back">
  <div class="work-photo" role="img" aria-label="Foto: Monteur mit Arbeitshandschuh am Laptop auf einem Solardach"></div>

  <div class="info info--top">
    <h2 class="info__title">Zuverlässige Konstruktionen</h2>
    <p>Sehr günstige Einkaufspreise und hervorragende Qualität bei den Unterkonstruktionssystemen durch die langjährige Erfahrung der NORVAL mit Herstellern und Lieferanten aus dem DACH-Gebiet.</p>
    <p>Die 100%ige Liefertreue und Qualität wird durch die langjährige Produktions­erfahrung der NORVAL und die ständige Überwachung der Lieferanten sicher­gestellt.</p>
  </div>

  <div class="product-photo" role="img" aria-label="Produktbild: Aluminium-Klemme mit Hammerkopfschraube"></div>

  <svg class="banner" width="476" height="675" viewBox="0 0 476 675" aria-hidden="true">
    <polygon points="381,330 428,330 444,366 397,366" fill="var(--brand-pale)"/>
    <polygon points="0,357 392,357 420,417 0,417" fill="var(--brand-light)"/>
    <polygon points="0,278 331,278 384,397 0,397" fill="var(--brand)"/>
  </svg>

  <div class="contact">
    <h2 class="contact__title">Lassen Sie sich beraten!</h2>
    <p class="contact__line contact__line--strong">KT Sonnwerk Energy GmbH,</p>
    <p class="contact__line">Haselgrundweg 14, 80469 München</p>
    <p class="contact__line">089 315 884 27</p>
    <p class="contact__line">info@ktsonnwerk-example.com</p>
    <p class="contact__line">www.ktsonnwerk-example.com</p>
  </div>

  <div class="info info--bottom">
    <h2 class="info__title">Optimales Montagesystem</h2>
    <p>Sicherer Verschluss und Verbindung der Dachhaken mit den Profilschienen. Die Profilschiene mit Hammerkopf­schraube ist universell einsetzbar und bietet eine hohe Flexibilität.</p>
    <p>Durch unsere Patente und das Ge­brauchsmuster können wir die Monta­gezeit enorm reduzieren.</p>
  </div>
</section>

</body>
</html>
```